label for coconut oil

A label to go on bottles of organic virgin coconut oil.
Fresh looking green stylised coconut,un cluttered,white or natural background,produce of Philipines,easy to reproduce,
will also use for other coconut products.
Portrait and landscape options.
Want it to look crafty,not to commercial,simple.
Company name is Amber Ridge but does not have to be included[can go on back of bottle with nutritional details]

```html
<!DOCTYPE html>
<html lang="en">
<head>
<meta charset="utf-8">
<title>Virgin Coconut Oil – Label Options</title>
<link rel="stylesheet" href="https://fonts.googleapis.com/css2?family=Sniglet:wght@400;800&display=swap">
<style>
  :root {
    --page: #ffffff;
    --olive: #7a7246;
    --lime: #a7c02a;
    --lime-bright: #a9c81e;
    --leaf-pale: #dfe9bd;
    --leaf-shade: #b9cc7a;
  }
  html, body {
    margin: 0;
    padding: 0;
    width: 1200px;
    height: 960px;
    overflow: hidden;
    background: var(--page);
  }
  .sheet {
    position: relative;
    width: 1200px;
    height: 960px;
  }
  .label {
    position: absolute;
    background: var(--olive);
    border-radius: 6px;
    overflow: hidden;
    font-family: "Sniglet", "Trebuchet MS", sans-serif;
    color: var(--lime);
  }
  .label--framed { left: 124px; top: 116px; width: 438px; height: 724px; }
  .label--plain  { left: 620px; top: 120px; width: 446px; height: 716px; }

  .label__frame {
    position: absolute;
    inset: 12px;
    border: 3px solid var(--lime);
    border-radius: 3px;
  }
  .label__title {
    position: absolute;
    margin: 0;
    line-height: 1;
    font-weight: 400;
  }
  .title__virgin {
    position: absolute;
    font-size: 48px;
    font-weight: 400;
    letter-spacing: 1px;
  }
  .title__coconut {
    position: absolute;
    font-size: 80px;
    font-weight: 800;
    letter-spacing: -1px;
  }
  .title__oil {
    position: absolute;
    font-size: 80px;
    font-weight: 800;
  }
  .label--framed .title__virgin  { left: 100px; top: 46px; }
  .label--framed .title__coconut { left: 24px;  top: 92px; }
  .label--framed .title__oil     { left: 300px; top: 164px; }
  .label--plain .title__virgin   { left: 108px; top: 14px; }
  .label--plain .title__coconut  { left: 30px;  top: 60px; }
  .label--plain .title__oil      { left: 306px; top: 132px; }

  .label__organic {
    position: absolute;
    margin: 0;
    display: flex;
    flex-direction: column;
    align-items: center;
    font-size: 40px;
    font-weight: 400;
    line-height: 56px;
  }
  .label--framed .label__organic { left: 26px; top: 264px; width: 60px; }
  .label--plain .label__organic  { left: 12px; top: 270px; width: 60px; }

  .label__leaf {
    position: absolute;
    border-radius: 8px 0 0 0;
  }
  .label--framed .label__leaf {
    left: 152px; top: 290px; width: 274px; height: 418px;
    background: linear-gradient(140deg, var(--leaf-pale) 0%, var(--leaf-shade) 55%, var(--leaf-pale) 100%);
  }
  .label--plain .label__leaf {
    left: 130px; top: 264px; width: 310px; height: 446px;
    background: linear-gradient(140deg, var(--lime-bright) 0%, #8fa52a 55%, var(--lime-bright) 100%);
  }
</style>
</head>
<body>
<main class="sheet">
  <section class="label label--framed">
    <div class="label__frame"></div>
    <h1 class="label__title">
      <span class="title__virgin">Virgin</span>
      <span class="title__coconut">Coconut</span>
      <span class="title__oil">Oil</span>
    </h1>
    <p class="label__organic"><span>O</span><span>r</span><span>g</span><span>a</span><span>n</span><span>i</span><span>c</span></p>
    <div class="label__leaf" role="img" aria-label="Stylised coconut palm fronds in pale green"></div>
  </section>

  <section class="label label--plain">
    <h1 class="label__title">
      <span class="title__virgin">Virgin</span>
      <span class="title__coconut">Coconut</span>
      <span class="title__oil">Oil</span>
    </h1>
    <p class="label__organic"><span>O</span><span>r</span><span>g</span><span>a</span><span>n</span><span>i</span><span>c</span></p>
    <div class="label__leaf" role="img" aria-label="Stylised coconut palm fronds in lime green"></div>
  </section>
</main>
</body>
</html>
```